Zarvo! Next Steps?, Bail Bond Company Check-in App , Court date, Court Reminders, Payments

Zarvo!
Next Steps?
WINNER OF THIS CONTEST WILL HAVE OPPORTUNITY TO DESIGN CUSTOMIZE SOME OUR COMPANY PAGES AFTER CONTEST!
Check-in with your Bail agent via pic/video
Receive Court reminders
Make a payments

Basically this app is a portal to 3rd party bail companies.
The idea is for the person whom makes bail downloads the Zarvo app from App Store.
Then they select a bail bond company.
This would be similar to a restaurant, real estate agent, insurance agent,,app where we could populate bail bond companies by client location or by typing in name of bail company.
We would like the ability to customize each bail bond company landing pages but are open to a global concept. when you click the bail bond company location it would have the logos for that company so the bail bond company screens would need to be customizeble
The app will require a photo or video check-in that is date and time
stamped with a gps location stored in check-in history
Check-in can be scheduled or random or voluntary
Voluntary and Scheduled Check-ins would require check-in button
Random would be via alert or text

The app should be able to receive court date updates
The app should allow clients to make payments to bail bond company
we need
ZARVO! landing page
client registration screens, check-in screens, available bail bond company screens for client to choose from
client registration page should include
name
email address
phone number
picture
home address
work address
date of birth
this app is different from our u-trak app. this is a bail bond check-in app for third party bail bond companies.
landing page should be ZARVO! Next Steps?
ZARVO ! Registration
Find your bail bond Company should list bail bond companies near me and search bar for searching bail bond companies by name
Next landing pages would be customizable for the third party bail bond companies
these would include pages for
check-ins via pics/videos
payment page
court reminders
contact information for bail bond companies
Zarvo Pages include
initial landing page
registration page
search bail companies

Bail bond company pages should include
Bali bond company landing page
Use KELNOR BAIL BOND COMPANY as example
contact information for bail company
check-in page
payment page
court reminder page
Updates

Low designer entries

Low designer entries

Sick

Sick

Sick

Target Market(s)

Court Defendants, Probation ,jails, sheriffs, judges, attorneys

Industry/Entity Type

justice, law enforcement, courts,

Requirements
Must have
• Check-in via pic/video, ability to receive court date reminders, make paymentswe need client registration screens, check-in screens, available bail bond company screens for client to choose from
Nice to have
• Professional easy to navigate intuitive customizable to 3rd party bail bond companies, logos,phone numbers etc.
Should not have
• unprofessional graphics,

```html
<!DOCTYPE html>
<html lang="en">
<head>
<meta charset="utf-8">
<title>Kelnor Bail Bonds – Agent Home</title>
<link rel="stylesheet" href="https://fonts.googleapis.com/css2?family=Roboto:wght@400;500;700&display=swap">
<style>
  :root{
    --hero-blue:#7fa2e8;
    --card-tint:rgba(255,255,255,0.2);
    --action-blue:#5b87e3;
    --white:#ffffff;
    --ink:#111111;
    --muted:#555555;
    --page-grey:#f6f6f6;
    --tile-border:#e3e3e3;
    --alert-red:#e23b3b;
    --logo-blue:#1f4fa0;
  }
  *{margin:0;padding:0;box-sizing:border-box}
  html,body{width:1200px;height:2428px;overflow:hidden}
  body{font-family:'Roboto',sans-serif;background:var(--page-grey);position:relative;color:var(--ink)}

  .hero{position:absolute;left:0;top:0;width:1200px;height:1363px;background:var(--hero-blue);color:var(--white)}
  .status-bar{position:absolute;left:60px;top:36px;right:60px;height:64px;display:flex;justify-content:space-between;align-items:center}
  .status-time{font-size:48px;font-weight:500}
  .status-icons{display:flex;gap:18px;align-items:center}
  .notify-bell{position:absolute;left:1068px;top:146px;width:72px;height:72px}

  .agency-badge{position:absolute;left:62px;top:225px;width:340px;height:340px;border-radius:50%;background:var(--white);display:flex;align-items:center;justify-content:center;box-shadow:0 6px 14px rgba(0,0,0,0.15)}
  .agency-badge span{color:var(--logo-blue);font-weight:700;font-size:66px;letter-spacing:2px}
  .agency-name{position:absolute;left:464px;top:280px;font-size:64px;font-weight:700}
  .agency-address{position:absolute;left:474px;top:380px;display:flex;gap:22px;font-size:40px;line-height:48px;width:640px}
  .agency-address svg{flex:none;margin-top:6px}

  .info-card{position:absolute;background:var(--card-tint);border-radius:30px;padding:44px 46px}
  .info-label{font-size:52px;font-weight:400}
  .info-value{font-size:70px;font-weight:400;margin-top:14px;padding-left:8px}
  .court-card{left:56px;top:628px;width:544px;height:255px}
  .balance-card{left:690px;top:628px;width:451px;height:255px}
  .checkin-card{left:56px;top:965px;width:1085px;height:255px}
  .checkin-button{position:absolute;left:713px;top:76px;width:288px;height:109px;border-radius:24px;background:var(--action-blue);color:var(--white);font:500 44px 'Roboto',sans-serif;border:none;box-shadow:0 4px 10px rgba(0,0,0,0.15)}

  .menu-grid{position:absolute;left:27px;top:1414px;display:grid;grid-template-columns:repeat(3,368px);grid-template-rows:repeat(2,367px);column-gap:17px;row-gap:15px}
  .menu-tile{position:relative;background:var(--white);border:2px solid var(--tile-border);border-radius:14px;display:flex;flex-direction:column;align-items:center;justify-content:center;gap:36px;box-shadow:0 3px 8px rgba(0,0,0,0.06)}
  .menu-tile svg{width:96px;height:96px}
  .menu-label{font-size:42px;color:var(--ink)}
  .alert-dot{position:absolute;top:22px;right:30px;width:24px;height:24px;border-radius:50%;background:var(--alert-red)}

  .tab-bar{position:absolute;left:0;top:2216px;width:1200px;height:212px;background:var(--page-grey);border-top:2px solid #dedede;display:grid;grid-template-columns:repeat(4,1fr);padding:0 20px}
  .tab{display:flex;flex-direction:column;align-items:center;padding-top:34px;gap:10px;color:var(--muted);font-size:38px}
  .tab svg{width:72px;height:72px}
  .tab.active{color:var(--action-blue)}
</style>
</head>
<body>
  <header class="hero">
    <div class="status-bar">
      <span class="status-time">9:41</span>
      <div class="status-icons">
        <svg width="56" height="36" viewBox="0 0 56 36"><rect x="0" y="24" width="9" height="12" rx="2" fill="#fff"/><rect x="15" y="17" width="9" height="19" rx="2" fill="#fff"/><rect x="30" y="9" width="9" height="27" rx="2" fill="#fff"/><rect x="45" y="0" width="9" height="36" rx="2" fill="#fff"/></svg>
        <svg width="52" height="38" viewBox="0 0 52 38"><path d="M26 36 L32 29 A9 9 0 0 0 20 29 Z" fill="#fff"/><path d="M12 22 A20 20 0 0 1 40 22" stroke="#fff" stroke-width="6" fill="none" stroke-linecap="round"/><path d="M4 13 A31 31 0 0 1 48 13" stroke="#fff" stroke-width="6" fill="none" stroke-linecap="round"/></svg>
        <svg width="80" height="38" viewBox="0 0 80 38"><rect x="2" y="2" width="68" height="34" rx="9" stroke="#fff" stroke-width="3" fill="none"/><rect x="7" y="7" width="58" height="24" rx="5" fill="#fff"/><rect x="73" y="13" width="5" height="12" rx="2" fill="#fff"/></svg>
      </div>
    </div>

    <svg class="notify-bell" viewBox="0 0 72 72" aria-label="Notifications">
      <path d="M16 50 V32 a18 18 0 0 1 36 0 V50 Z M10 50 H58" stroke="#fff" stroke-width="5" fill="none" stroke-linejoin="round" stroke-linecap="round"/>
      <path d="M28 58 a6 6 0 0 0 12 0" stroke="#fff" stroke-width="5" fill="none"/>
      <circle cx="56" cy="12" r="10" fill="var(--alert-red)"/>
    </svg>

    <div class="agency-badge"><span>KELNOR</span></div>
    <h1 class="agency-name">Kelnor Bail Bonds</h1>
    <p class="agency-address">
      <svg width="30" height="40" viewBox="0 0 30 40"><path d="M15 37 C6 26 3 20 3 14 a12 12 0 0 1 24 0 c0 6-3 12-12 23Z" stroke="#fff" stroke-width="3" fill="none"/><circle cx="15" cy="14" r="4.5" stroke="#fff" stroke-width="3" fill="none"/></svg>
      <span>4120, Harlow Street, Bren&shy;ton, CA 90000</span>
    </p>

    <section class="info-card court-card">
      <div class="info-label">Next court date:</div>
      <div class="info-value">10 Dec 2022</div>
    </section>
    <section class="info-card balance-card">
      <div class="info-label">Balance</div>
      <div class="info-value">$1,000.00</div>
    </section>
    <section class="info-card checkin-card">
      <div class="info-label">Next check-in:</div>
      <div class="info-value">05 Dec 2022</div>
      <button class="checkin-button">Check-in</button>
    </section>
  </header>

  <nav class="menu-grid">
    <div class="menu-tile"><span class="alert-dot"></span>
      <svg viewBox="0 0 48 48" fill="none" stroke="#111" stroke-width="3.2" stroke-linecap="round" stroke-linejoin="round"><path d="M20 34 C11 24 9 19 9 15 a11 11 0 0 1 22 0 c0 4-2 9-11 19Z"/><circle cx="20" cy="15" r="4"/><path d="M22 40 l4 4 l8-8 M28 40 l4 4 l8-8"/></svg>
      <span class="menu-label">Check-ins</span></div>
    <div class="menu-tile"><span class="alert-dot"></span>
      <svg viewBox="0 0 48 48" fill="#111"><rect x="6" y="10" width="36" height="32" rx="3"/><rect x="10" y="20" width="28" height="18" fill="#fff"/><rect x="13" y="5" width="4" height="9" rx="1"/><rect x="31" y="5" width="4" height="9" rx="1"/><rect x="13" y="24" width="8" height="7"/></svg>
      <span class="menu-label">Court dates</span></div>
    <div class="menu-tile">
      <svg viewBox="0 0 48 48" fill="none" stroke="#111" stroke-width="2.6" stroke-linecap="round" stroke-linejoin="round"><path d="M4 36 l8-10 l10-6 h8 l-8 7 M4 36 h30 l10-6"/><path d="M16 22 l6-10 h20 v14 h-14"/><circle cx="36" cy="26" r="5" fill="#111"/></svg>
      <span class="menu-label">Pay</span></div>
    <div class="menu-tile">
      <svg viewBox="0 0 48 48" fill="none" stroke="#111" stroke-width="3.2" stroke-linecap="round"><circle cx="24" cy="24" r="19"/><path d="M30 17 c-2-2-4-3-6-3 c-4 0-6 2-6 5 c0 6 12 3 12 9 c0 3-3 5-6 5 c-3 0-5-1-7-3 M24 10 v4 M24 33 v5"/></svg>
      <span class="menu-label">Account info</span></div>
    <div class="menu-tile">
      <svg viewBox="0 0 48 48" fill="none" stroke="#111" stroke-width="3.2" stroke-linecap="round"><circle cx="24" cy="24" r="19"/><path d="M24 22 v12"/><circle cx="24" cy="15" r="1.5" fill="#111"/></svg>
      <span class="menu-label">About us</span></div>
    <div class="menu-tile">
      <svg viewBox="0 0 48 48" fill="none" stroke="#111" stroke-width="3.2" stroke-linecap="round"><circle cx="18" cy="15" r="8"/><path d="M4 42 c0-9 6-15 14-15 c8 0 14 6 14 15 Z"/><path d="M32 14 h12 M35 22 h9 M38 30 h6"/></svg>
      <span class="menu-label">Contact</span></div>
  </nav>

  <footer class="tab-bar">
    <div class="tab"><svg viewBox="0 0 36 36" fill="none" stroke="#555" stroke-width="2.6" stroke-linecap="round"><circle cx="16" cy="16" r="12"/><path d="M25 25 l7 7"/></svg><span>Search</span></div>
    <div class="tab active"><svg viewBox="0 0 36 36" fill="none" stroke="#5b87e3" stroke-width="2.6" stroke-linejoin="round"><circle cx="18" cy="11" r="7"/><path d="M5 33 v-5 c0-5 4-8 8-8 h10 c4 0 8 3 8 8 v5 Z M18 20 v6"/></svg><span>My Agent</span></div>
    <div class="tab"><svg viewBox="0 0 36 36" fill="none" stroke="#555" stroke-width="2.6" stroke-linejoin="round"><path d="M18 3 L31 10.5 V25.5 L18 33 L5 25.5 V10.5 Z"/><circle cx="18" cy="18" r="5"/></svg><span>Setting</span></div>
    <div class="tab"><svg viewBox="0 0 36 36" fill="none" stroke="#555" stroke-width="2.6"><circle cx="18" cy="18" r="15"/><circle cx="18" cy="14" r="5"/><path d="M8 29 c2-5 6-7 10-7 s8 2 10 7"/></svg><span>Profile</span></div>
  </footer>
</body>
</html>
```